Need a book cover design for a Lumora Book on Herbal Remedies

I need a book cover for my new ebook, here are the details:
Title: Meadow Cures
Sub-Heading: Buried Ancient Garden Tonics
Reclaiming the Wisdom of Roots for Everyday Wellness and Strength
Author: Nora Belcourt

```html
<!DOCTYPE html>
<html lang="en">
<head>
<meta charset="utf-8">
<title>Meadow Cures — Nora Belcourt</title>
<link rel="stylesheet" href="https://fonts.googleapis.com/css2?family=Amatic+SC:wght@700&family=Patrick+Hand+SC&display=swap">
<style>
  :root {
    --page-bg: #c3c8dc;
    --cover-dark: #140f0c;
    --cover-mid: #2b2119;
    --leaf: #2f3a24;
    --lavender: #5b4d74;
    --title-yellow: #e4e33d;
    --title-green: #8ee55a;
    --text-light: #f4f1ea;
  }
  * { margin: 0; padding: 0; box-sizing: border-box; }
  html, body {
    width: 1200px;
    height: 2952px;
    overflow: hidden;
    background: var(--page-bg);
  }
  .book-cover {
    position: absolute;
    left: 100px;
    top: 675px;
    width: 1000px;
    height: 1602px;
    overflow: hidden;
    box-shadow: 0 10px 30px rgba(40, 40, 70, 0.25);
  }
  .cover-artwork {
    position: absolute;
    inset: 0;
    background:
      radial-gradient(ellipse 45% 30% at 82% 22%, rgba(91, 77, 116, 0.75), transparent 70%),
      radial-gradient(ellipse 40% 25% at 20% 28%, rgba(74, 58, 86, 0.6), transparent 70%),
      radial-gradient(ellipse 35% 18% at 45% 20%, rgba(47, 58, 36, 0.8), transparent 70%),
      radial-gradient(ellipse 60% 25% at 55% 62%, rgba(70, 48, 32, 0.55), transparent 70%),
      radial-gradient(ellipse 55% 18% at 50% 85%, rgba(60, 44, 34, 0.6), transparent 70%),
      linear-gradient(180deg, var(--cover-dark) 0%, var(--cover-mid) 55%, var(--cover-dark) 100%);
  }
  .cover-text {
    position: absolute;
    left: 0;
    width: 100%;
    text-align: center;
    line-height: 1;
  }
  .series-line {
    top: 72px;
    font-family: "Amatic SC", cursive;
    font-weight: 700;
    font-size: 50px;
    letter-spacing: 7px;
    color: var(--text-light);
  }
  .title {
    font-family: "Patrick Hand SC", cursive;
    font-size: 232px;
    letter-spacing: -2px;
  }
  .title-first { top: 470px; color: var(--title-yellow); }
  .title-second { top: 690px; color: var(--title-green); }
  .subtitle {
    top: 955px;
    font-family: "Patrick Hand SC", cursive;
    font-size: 60px;
    line-height: 66px;
    color: var(--text-light);
  }
  .author {
    top: 1355px;
    font-family: "Amatic SC", cursive;
    font-weight: 700;
    font-size: 82px;
    letter-spacing: 8px;
    color: var(--text-light);
  }
</style>
</head>
<body>
  <div class="book-cover">
    <div class="cover-artwork" role="img" aria-label="Dark rustic still life of lavender bunches, basil leaves, clay pots, corked apothecary bottles and scattered dried spices on a wooden table"></div>
    <p class="cover-text series-line">BURIED ANCIENT GARDEN TONICS</p>
    <h1>
      <span class="cover-text title title-first">MEADOW</span>
      <span class="cover-text title title-second">CURES</span>
    </h1>
    <p class="cover-text subtitle">RECLAIMING THE<br>WISDOM OF ROOTS FOR EVERYDAY<br>WELLNESS AND STRENGTH</p>
    <p class="cover-text author">NORA BELCOURT</p>
  </div>
</body>
</html>
```